Personal Finance e-commerce website needs a simple budget design

Hello! I am starting to sell downloadable and printable budget planners, as shown in the attached file, for people to plan ahead on their personal finances. <br/><br/>I want to see a one-page design with similar columns (for example, "Expenses, Budget, and Actual"). I would also like to see the basic formula ("Net Income = Gross income - Total Expenses") somewhere on the design. Finally, I want the design to remain mostly minimalistic and simple for the average person to plan their personal monthly budgets.<br/><br/>However, other than that, the overall design, layout, and colors will be at the graphic designer's choice. If you have any questions for me, please let me know. Thank you for your time!

Industry/Entity Type

Financial Planning

Colors

Designer to choose colors to be used in the design.

Requirements
Must have
• I want to see a one-page design with similar columns (for example, "Expenses, Budget, and Actual").
• I want the design to remain mostly minimalistic and simple for the average person to plan their personal monthly budgets.
Nice to have
• I would also like to see the basic formula ("Net Income = Gross income - Total Expenses") somewhere on the design.

```html
<!DOCTYPE html>
<html lang="en">
<head>
<meta charset="utf-8">
<title>Basic Monthly Budget</title>
<link rel="stylesheet" href="https://fonts.googleapis.com/css2?family=Titillium+Web:wght@300;400;700&family=Signika:wght@600&family=Open+Sans:wght@400&display=swap">
<style>
  :root {
    --bg: #2d3e50;
    --card: #ffffff;
    --row: #edf0f8;
    --green: #22c76a;
    --green-dark: #0f5a2e;
    --teal: #1f8fb0;
    --slate: #4b4560;
    --hint: #b9bcc2;
    --red: #f13a3a;
    --note: #d6d9de;
  }
  * { margin: 0; padding: 0; box-sizing: border-box; }
  html, body { width: 1200px; height: 1006px; overflow: hidden; }
  body {
    position: relative;
    background: var(--bg);
    font-family: "Titillium Web", sans-serif;
  }
  .title {
    position: absolute;
    left: 69px;
    top: 46px;
    font-family: "Signika", sans-serif;
    font-weight: 600;
    font-size: 41px;
    letter-spacing: -0.3px;
    color: var(--green);
    -webkit-text-stroke: 1px var(--green-dark);
    text-shadow: 0 0 6px rgba(0,0,0,0.55), 0 2px 4px rgba(0,0,0,0.5);
  }
  .sheet {
    position: absolute;
    left: 63px;
    top: 144px;
    width: 1081px;
    height: 633px;
    background: var(--card);
    border-radius: 9px;
  }
  .col-head {
    position: absolute;
    top: 33px;
    height: 53px;
    padding-left: 28px;
    border-left: 2px solid;
  }
  .col-head h2 {
    font-size: 19px;
    line-height: 1;
    font-weight: 300;
    margin-top: -2px;
  }
  .col-head h2 strong { font-weight: 700; }
  .col-head p {
    font-size: 19px;
    font-weight: 300;
    color: var(--hint);
    margin-top: 16px;
    line-height: 1;
  }
  .col-expenses { left: 35px; border-color: var(--teal); color: var(--teal); }
  .col-budget { left: 384px; border-color: var(--green); color: var(--green); }
  .col-actual { left: 749px; border-color: var(--slate); color: var(--slate); }
  .entry-row {
    position: absolute;
    left: 23px;
    width: 1035px;
    height: 34px;
    background: var(--row);
    border-radius: 6px;
  }
  .formula {
    position: absolute;
    left: 64px;
    top: 806px;
    font-family: "Open Sans", sans-serif;
    font-size: 23px;
    line-height: 32px;
    color: var(--green);
    text-shadow: 0 2px 4px rgba(0,0,0,0.45);
    white-space: nowrap;
  }
  .formula .minus, .formula .expenses { color: var(--red); }
  .formula .eq { margin: 0 4px; }
  .term-note {
    position: absolute;
    top: 857px;
    width: 120px;
    margin-left: -60px;
    text-align: center;
    font-family: "Open Sans", sans-serif;
    font-size: 18px;
    line-height: 23px;
    color: var(--note);
  }
</style>
</head>
<body>
  <h1 class="title">Basic Monthly Budget</h1>

  <section class="sheet">
    <div class="col-head col-expenses">
      <h2><strong>Expenses</strong> (Category)</h2>
      <p>Custom Category</p>
    </div>
    <div class="col-head col-budget">
      <h2><strong>Budget</strong> (USD)</h2>
      <p>What you plan to spend</p>
    </div>
    <div class="col-head col-actual">
      <h2><strong>Actual</strong> (USD)</h2>
      <p>What you actually spent</p>
    </div>

    <div class="entry-row" style="top:106px"></div>
    <div class="entry-row" style="top:178px"></div>
    <div class="entry-row" style="top:249px"></div>
    <div class="entry-row" style="top:321px"></div>
    <div class="entry-row" style="top:393px; left:24px"></div>
    <div class="entry-row" style="top:466px; left:24px"></div>
    <div class="entry-row" style="top:539px; left:24px"></div>
  </section>

  <p class="formula">Net Income <span class="eq">=</span> Gross Income <span class="minus">-</span> <span class="expenses">Expenses</span></p>

  <p class="term-note" style="left:118px">How much money you kept</p>
  <p class="term-note" style="left:274px">How much money you earned</p>
  <p class="term-note" style="left:420px">Actual Expenses</p>
</body>
</html>
```